Vegetable Grower Expo Backdrop

I need an 8x8 backdrop for an expo booth. We are a vegetable grower and have very limited graphics to work with. I have uploaded our logo which may not be the correct format and need to be updated for quality to print at that size. Need something quick and simple. Expo is August 18th

Target Market(s)

Retail and Wholesale buyers

Industry/Entity Type

Produce

Colors

Designer to choose colors to be used in the design.

Requirements
Must have
• Logo
Nice to have
• I am open to ideas!
Should not have
• Keep it simple and bottom 1/4 will be covered with samples so focus on top 3/4 of banner

```html
<!DOCTYPE html>
<html lang="en">
<head>
<meta charset="UTF-8">
<title>Vegetable Grower Expo Backdrop</title>
<link href="https://fonts.googleapis.com/css2?family=Poppins:wght@500;600;700;800&display=swap" rel="stylesheet">
<style>
  :root {
    --page-bg: #c4c4c4;
    --forest: #0a4624;
    --lime: #9fcb3b;
    --white: #ffffff;
  }
  * { margin: 0; padding: 0; box-sizing: border-box; }
  html, body {
    width: 721px; height: 1200px; overflow: hidden;
    background: var(--page-bg);
    font-family: "Poppins", sans-serif;
  }
  .backdrop {
    position: absolute; left: 0; top: 240px;
    width: 721px; height: 721px;
    background: var(--forest);
    overflow: hidden;
  }
  .produce-photo {
    position: absolute; left: 0; top: 142px; width: 721px; height: 390px;
    background:
      radial-gradient(ellipse at 20% 40%, rgba(217,138,43,0.22), transparent 55%),
      radial-gradient(ellipse at 80% 35%, rgba(184,65,44,0.22), transparent 55%),
      radial-gradient(ellipse at 50% 70%, rgba(63,122,46,0.35), transparent 60%),
      linear-gradient(180deg, var(--forest) 0%, #0f5229 25%, #125a2c 70%, var(--forest) 100%);
  }
  .sketch-border {
    position: absolute; left: 0; top: 512px; width: 721px; height: 209px;
    background: linear-gradient(180deg, transparent 0%, rgba(255,255,255,0.05) 40%, rgba(255,255,255,0.08) 100%);
  }
  .brand {
    position: absolute; left: 0; top: 78px; width: 721px;
    display: flex; align-items: center; justify-content: center; gap: 14px;
  }
  .brand-dot {
    width: 40px; height: 40px; border-radius: 50%;
    background: var(--lime);
  }
  .brand-name {
    color: var(--lime); font-weight: 600; font-size: 28px; line-height: 1;
  }
  .headline {
    position: absolute; left: 0; width: 721px; text-align: center;
    font-weight: 700; line-height: 1;
  }
  .headline-top { top: 171px; font-size: 74px; color: var(--white); text-shadow: 0 3px 6px rgba(0,0,0,0.45); }
  .headline-mid { top: 240px; font-size: 74px; color: var(--lime); text-shadow: 0 3px 6px rgba(0,0,0,0.35); }
  .expo-word { position: absolute; left: 0; top: 330px; }
  .event-year {
    position: absolute; left: 0; width: 721px; top: 512px; text-align: center;
    font-weight: 700; font-size: 32px; color: var(--lime); letter-spacing: 12px; padding-left: 12px;
  }
  .event-site {
    position: absolute; left: 0; width: 721px; top: 556px; text-align: center;
    font-weight: 600; font-size: 17px; color: var(--white);
  }
</style>
</head>
<body>
  <main class="backdrop">
    <div class="produce-photo" role="img" aria-label="Faded photograph of assorted fresh vegetables"></div>
    <div class="sketch-border" role="img" aria-label="White line sketches of vegetables: celery, asparagus, tomatoes, peppers, bok choy and leaves"></div>

    <header class="brand">
      <div class="brand-dot"></div>
      <div class="brand-name">VALLEYSIDE GROWERS</div>
    </header>

    <h1 class="headline headline-top">VEGETABLE</h1>
    <h2 class="headline headline-mid">GROWER</h2>

    <svg class="expo-word" width="721" height="180" viewBox="0 0 721 180">
      <defs>
        <linearGradient id="produce-fill" x1="0" y1="0" x2="1" y2="1">
          <stop offset="0" stop-color="#d98a2b"/>
          <stop offset="0.35" stop-color="#b8412c"/>
          <stop offset="0.65" stop-color="#e2b23a"/>
          <stop offset="1" stop-color="#3f7a2e"/>
        </linearGradient>
      </defs>
      <text x="366" y="158" text-anchor="middle" textLength="543" lengthAdjust="spacingAndGlyphs"
            font-family="Poppins, sans-serif" font-weight="600" font-size="210"
            fill="url(#produce-fill)" stroke="#9fcb3b" stroke-width="3"
            role="img" aria-label="EXPO, letters filled with a photograph of fresh vegetables">EXPO</text>
    </svg>

    <p class="event-year">2025</p>
    <p class="event-site">www.valleysidegrowers.com</p>
  </main>
</body>
</html>
```